M&A Advisory firm needs elegant and powerful letterhead

We need a powerful but elegant letterhead to engage with the international financial industry.

Target Market(s)

New York and International Financial Industry

Industry/Entity Type

Finance

Font styles to use
Other font styles liked:
• Poppins

Requirements
Must have
• 437 W 82nd Street 14th Floor New York, NY 10024 O: +1 (212) 555 0147 F: +1 (212) 555 0182

```html
<!DOCTYPE html>
<html lang="en">
<head>
<meta charset="utf-8">
<title>Norvane Letterhead</title>
<link href="https://fonts.googleapis.com/css2?family=Poppins:wght@400;500&display=swap" rel="stylesheet">
<style>
  :root {
    --backdrop: #dcdcdc;
    --paper: #f8f8f8;
    --brand-blue: #1b4e94;
    --text-grey: #4a4a4a;
    --rule-grey: #b5b5b5;
  }
  * { margin: 0; padding: 0; box-sizing: border-box; }
  html, body {
    width: 1153px;
    height: 1200px;
    overflow: hidden;
    background: var(--backdrop);
    font-family: "Poppins", sans-serif;
  }
  .letterhead {
    position: absolute;
    left: 174px;
    top: 40px;
    width: 804px;
    height: 1120px;
    background: var(--paper);
    box-shadow: 0 6px 18px rgba(0,0,0,0.12);
  }
  .brand {
    position: absolute;
    left: 79px;
    top: 74px;
    display: flex;
    align-items: center;
    gap: 14px;
  }
  .brand-dot {
    width: 30px;
    height: 30px;
    border-radius: 50%;
    background: var(--brand-blue);
  }
  .brand-name {
    font-size: 42px;
    font-weight: 400;
    line-height: 1;
    letter-spacing: 1px;
    color: var(--brand-blue);
  }
  .contact {
    position: absolute;
    left: 566px;
    top: 60px;
    font-size: 12.5px;
    line-height: 16px;
    color: var(--text-grey);
  }
  .contact-address { margin-bottom: 8px; }
  .contact-line {
    display: flex;
    align-items: center;
    gap: 6px;
    height: 19px;
  }
  .contact-icon { width: 14px; height: 13px; flex: none; }
  .header-rule {
    position: absolute;
    left: 79px;
    top: 157px;
    width: 644px;
    height: 1px;
    background: var(--rule-grey);
  }
</style>
</head>
<body>
  <main class="letterhead">
    <header>
      <div class="brand">
        <span class="brand-dot"></span>
        <span class="brand-name">NORVANE</span>
      </div>
      <address class="contact" style="font-style: normal;">
        <p class="contact-address">437 W 82nd Street 14th<br>Floor New York, NY 10024</p>
        <p class="contact-line">
          <svg class="contact-icon" viewBox="0 0 14 13" aria-label="Phone">
            <path d="M1 4.5 C1 1.5 13 1.5 13 4.5 L13 5.5 L10 5.5 L10 4 L4 4 L4 5.5 L1 5.5 Z" fill="#1b4e94"/>
            <path d="M3 6 L11 6 L12.5 12.5 L1.5 12.5 Z" fill="#1b4e94"/>
            <circle cx="7" cy="9.3" r="2" fill="#f8f8f8"/>
          </svg>
          +1 (212) 555 0147
        </p>
        <p class="contact-line">
          <svg class="contact-icon" viewBox="0 0 14 13" aria-label="Fax">
            <rect x="4" y="0.5" width="7" height="5" fill="none" stroke="#1b4e94" stroke-width="1.2"/>
            <rect x="0.5" y="5.5" width="13" height="5" fill="#1b4e94"/>
            <rect x="0.5" y="11" width="13" height="1.8" fill="#1b4e94"/>
          </svg>
          +1 (212) 555 0182
        </p>
      </address>
      <div class="header-rule"></div>
    </header>
  </main>
</body>
</html>
```